Packaging design - PROTEIN BALLS

PACKAGING
The packaging is a round carton roll, size: Ø73x180 mm, mockup sample enclosed, The label on the carton roll should have a size of 225x178 mm (width x height)

PRODUCT
Chrunchy, cheesy PROTEIN BALLS (100% pure cheese) with a huge amount of protein (65%), a lot of calcium and very low carbogydrates (3%). Diameter about 1.5 cm.

DESIGN
Since our customers are very sporty people, runner, bodybuilder, etc. The design must fit to this sporty customer segment.

FILES
We need the open data for InDesign with all fonts and pictures. If there are licenses tu buy, we will do it.

SUMMARY
1. SNACK
• Crunchy cheese balls with a diameter of about 1.5cm
• 3 different flavors: "Swiss Alpine Salt", "Provencale" and "Hot Chili"
• High in Protein (65%) and Calcium (2%)
• Low in carbohydrates (3%)

2. PACKAGING
• Carton roll, size: Ø73x180 mm
• Background can be every color, but we think a black one will be high premium.
• Maybe different sports are represented in the background, maybe also cheese
• Be creative
• Label applied, size: 225x178 mm

3. DESIGN
• Product name = (Cheese) PROTEIN BALLS
• 3 different colors for the 3 flavors "Swiss Alpine Salt", "Provencale" and "Hot Chili"
• HighProtein, High Calcium and LowCarb must be pointed out on the front
• Swissness: Swiss made must be pointed out
• fresh and young design, most customers are sporty people, pumper with a strong body awareness

TARGET CUSTOMER
Our main customers are extremely sporty people, who work very hard on their muscles and fitness, most of them are runners, cross fitnesser, bodybuilders, etc We will launch the product in fitness centers, in supplement shops and we are planning to make some stories with sporty influencer.

Serif
Sans Serif

• Cheese, naturalness, healthy, PROTEIN balls, muscles, Swissness must showed on the product.

```html
<!DOCTYPE html>
<html lang="en">
<head>
<meta charset="utf-8">
<title>Protein Balls – Hot Chilli label</title>
<link rel="stylesheet" href="https://fonts.googleapis.com/css2?family=Montserrat:wght@300;400;700;800&family=Luckiest+Guy&display=swap">
<style>
  :root {
    --stage-red: #a8191f;
    --stage-red-dark: #6a0f13;
    --label-black: #120809;
    --muscle-bright: #8e2630;
    --muscle-red: #5e1820;
    --muscle-deep: #2a0c10;
    --dumbbell-red: #6e2430;
    --dumbbell-shine: #a85a66;
    --bowl-wood: #c8955a;
    --bowl-wood-dark: #8f6234;
    --cheese-yellow: #f4dc3c;
    --cheese-deep: #e6b424;
    --chrome-light: #f4f4f4;
    --chrome-mid: #b8b8b8;
    --flavour-red: #c8262e;
    --claim-white: #f2f2f2;
    --origin-grey: #d0d0d0;
  }
  html, body {
    margin: 0;
    width: 1200px;
    height: 987px;
    overflow: hidden;
  }
  body {
    background: radial-gradient(ellipse at center, var(--stage-red) 0%, var(--stage-red-dark) 100%);
    font-family: "Montserrat", sans-serif;
    position: relative;
  }
  .label {
    position: absolute;
    left: 462px;
    top: 120px;
    width: 282px;
    height: 743px;
    background: var(--label-black);
    overflow: hidden;
  }
  .athlete-photo {
    position: absolute;
    inset: 0;
    background:
      radial-gradient(ellipse 60% 28% at 22% 20%, var(--muscle-bright) 0%, transparent 80%),
      radial-gradient(ellipse 55% 22% at 30% 46%, var(--muscle-red) 0%, transparent 85%),
      linear-gradient(180deg, var(--muscle-deep) 0%, #1c0a0d 55%, var(--label-black) 100%);
  }
  .cheese-bowl-photo {
    position: absolute;
    left: 82px;
    top: -80px;
    width: 400px;
    height: 400px;
  }
  .dumbbell-photo {
    position: absolute;
    left: -30px;
    top: 450px;
    width: 290px;
    height: 270px;
  }
  .headline {
    position: absolute;
    left: 0;
    right: 0;
    top: 372px;
    text-align: center;
    padding-left: 12px;
  }
  .tagline {
    font-family: "Luckiest Guy", "Impact", sans-serif;
    color: var(--chrome-light);
    font-size: 17px;
    letter-spacing: 1.5px;
    margin: 0 0 4px;
  }
  .product-name {
    margin: 0;
    font-weight: 800;
    font-size: 51px;
    line-height: 0.92;
    background: linear-gradient(180deg, var(--chrome-light) 0%, var(--chrome-mid) 100%);
    -webkit-background-clip: text;
    background-clip: text;
    color: transparent;
  }
  .flavour-tag {
    display: inline-block;
    margin-top: 14px;
    background: var(--flavour-red);
    color: var(--claim-white);
    font-family: "Luckiest Guy", "Impact", sans-serif;
    font-size: 16px;
    letter-spacing: 1px;
    padding: 4px 14px 2px;
  }
  .claims {
    position: absolute;
    right: 20px;
    top: 648px;
    text-align: right;
    color: var(--claim-white);
    font-size: 16px;
    line-height: 16px;
    font-weight: 300;
  }
  .claims strong { font-weight: 700; color: var(--claim-white); }
  .claims .origin {
    font-size: 13px;
    margin-top: 8px;
    color: var(--origin-grey);
  }
</style>
</head>
<body>
  <section class="label">
    <div class="athlete-photo" role="img" aria-label="Red-toned photo of a muscular athlete's shoulder and arm"></div>

    <svg class="cheese-bowl-photo" viewBox="0 0 400 400" role="img" aria-label="Wooden bowl full of crunchy cheese protein balls with chilli flakes">
      <defs>
        <radialGradient id="bowlWood" cx="50%" cy="50%" r="50%">
          <stop offset="88%" stop-color="var(--bowl-wood)"/>
          <stop offset="100%" stop-color="var(--bowl-wood-dark)"/>
        </radialGradient>
        <radialGradient id="bowlCheese" cx="50%" cy="45%" r="50%">
          <stop offset="0%" stop-color="var(--cheese-yellow)"/>
          <stop offset="100%" stop-color="var(--cheese-deep)"/>
        </radialGradient>
      </defs>
      <circle cx="200" cy="200" r="200" fill="url(#bowlWood)"/>
      <circle cx="200" cy="200" r="178" fill="url(#bowlCheese)"/>
    </svg>

    <svg class="dumbbell-photo" viewBox="0 0 290 270" role="img" aria-label="Red-toned chrome dumbbell held by the athlete">
      <defs>
        <radialGradient id="dumbbellTone" cx="45%" cy="50%" r="55%">
          <stop offset="0%" stop-color="var(--dumbbell-shine)"/>
          <stop offset="45%" stop-color="var(--dumbbell-red)"/>
          <stop offset="100%" stop-color="var(--label-black)" stop-opacity="0"/>
        </radialGradient>
      </defs>
      <rect width="290" height="270" fill="url(#dumbbellTone)"/>
    </svg>

    <div class="headline">
      <p class="tagline">CHRUNCHY, CHEESY</p>
      <h1 class="product-name">PROTEIN<br>BALLS</h1>
      <span class="flavour-tag">HOT CHILLI</span>
    </div>

    <div class="claims">
      <div>HIGH <strong>PROTEIN</strong></div>
      <div>HIGH <strong>CALCIUM</strong></div>
      <div>LOW <strong>CARB</strong></div>
      <div class="origin">SWISS MADE</div>
    </div>
  </section>
</body>
</html>
```